Business Card Design

I am a Special Event Consultant,I arrange and organise Special Events - Product Launches,Sponsorship and Product Displays.

I would like the TRV to be a feature of the design with 'Special Event Services" underneath - keep it very simple but creative using this information. So it is just the letters "TRV" with Event Services underneath.

(Simple Colours - Silver, Black, Grey - no bright colours - We work for Valdoren Kraft,QJX, Tavrelli So it is class and classic.)

Only my Name and mobile on the front.

Industry/Entity Type

Business

Contact Information for Business Card

FRONT
Jo Pettigrew
Tel: 0427 318906

BACK
Email: jo@trvoccasionhire.com.au

1208 Wexley Court,72 Ormond Lane
KELMSTON.Vic.3145.

```html
<!DOCTYPE html>
<html lang="en">
<head>
<meta charset="utf-8">
<title>TRV Event Services – Business Card</title>
<link href="https://fonts.googleapis.com/css2?family=Questrial&family=Didact+Gothic&display=swap" rel="stylesheet">
<style>
  :root {
    --page: #ffffff;
    --card-dark: #414141;
    --card-light: #5c5a59;
    --accent: #29abe2;
    --ink: #ffffff;
    --ink-soft: #ececec;
  }
  * { margin: 0; padding: 0; box-sizing: border-box; }
  html, body {
    width: 1200px; height: 1000px; overflow: hidden;
    background: var(--page);
  }
  .stage { position: relative; width: 1200px; height: 1000px; }
  .card {
    position: absolute;
    width: 603px; height: 372px;
    background: linear-gradient(115deg, var(--card-dark) 0%, var(--card-light) 100%);
    box-shadow: 3px 4px 6px rgba(0,0,0,0.28);
    color: var(--ink);
    font-family: "Didact Gothic", "Questrial", sans-serif;
  }
  .card--front { left: 111px; top: 145px; z-index: 2; }
  .card--back  { left: 486px; top: 484px; z-index: 1; }

  .wordmark {
    position: absolute;
    font-family: "Questrial", sans-serif;
    color: var(--accent);
    line-height: 1;
    letter-spacing: 1px;
  }
  .tagline {
    position: absolute;
    font-family: "Didact Gothic", sans-serif;
    font-style: italic;
    color: var(--ink);
    line-height: 1;
    white-space: nowrap;
    padding-bottom: 4px;
    border-bottom: 1.5px solid var(--accent);
  }
  .card--front .wordmark { left: 104px; top: 126px; font-size: 66px; }
  .card--front .tagline {
    left: 191px; top: 203px; font-size: 23px; letter-spacing: 9.3px; width: 306px;
  }
  .card--back .wordmark { left: 59px; top: 134px; font-size: 43px; }
  .card--back .tagline {
    left: 114px; top: 181px; font-size: 15px; letter-spacing: 5.9px; width: 197px;
  }

  .holder-name {
    position: absolute; left: 30px; top: 326px;
    font-size: 17px; letter-spacing: 3.2px;
  }
  .mobile {
    position: absolute; left: 399px; top: 324px;
    display: flex; align-items: center; gap: 8px;
    font-size: 18px; letter-spacing: 3.1px;
  }
  .address {
    position: absolute; left: 270px; top: 282px;
    font-style: normal; font-size: 15.5px; line-height: 22px;
    letter-spacing: 2px; color: var(--ink-soft);
  }
  .email {
    position: absolute; left: 271px; top: 328px;
    display: flex; align-items: center; gap: 7px;
    font-size: 15px; letter-spacing: 2px;
  }
  .icon { flex: none; }
</style>
</head>
<body>
<main class="stage">
  <section class="card card--front" aria-label="Business card front">
    <div class="wordmark">TRV</div>
    <div class="tagline">Event Services</div>
    <p class="holder-name">Jo Pettigrew</p>
    <p class="mobile">
      <svg class="icon" width="12" height="21" viewBox="0 0 12 21" aria-hidden="true">
        <rect x="0.9" y="0.9" width="10.2" height="19.2" rx="1.6" fill="none" stroke="#fff" stroke-width="1.6"/>
        <line x1="1" y1="16" x2="11" y2="16" stroke="#fff" stroke-width="1.2"/>
        <circle cx="6" cy="18.2" r="0.9" fill="#fff"/>
      </svg>
      <span>0427 318906</span>
    </p>
  </section>

  <section class="card card--back" aria-label="Business card back">
    <div class="wordmark">TRV</div>
    <div class="tagline">Event Services</div>
    <address class="address">1208 Wexley Court,<br>72 Ormond Lane Kelmston VIC 3145</address>
    <p class="email">
      <svg class="icon" width="18" height="13" viewBox="0 0 18 13" aria-hidden="true">
        <rect x="0.7" y="0.7" width="16.6" height="11.6" fill="none" stroke="#fff" stroke-width="1.4"/>
        <polyline points="0.7,0.7 9,7.5 17.3,0.7" fill="none" stroke="#fff" stroke-width="1.4"/>
        <line x1="0.7" y1="12.3" x2="6.5" y2="5.5" stroke="#fff" stroke-width="1.2"/>
        <line x1="17.3" y1="12.3" x2="11.5" y2="5.5" stroke="#fff" stroke-width="1.2"/>
      </svg>
      <span>jo@trvoccasionhire.com.au</span>
    </p>
  </section>
</main>
</body>
</html>
```